Stylish Business Card for Modern hair salon

I need a simple business card design using our salon logo and colours that are in the logo. We service clients of all ages but predominantly those in the 18 to 55 age range. We have a young staff and are looking to have a card that will present a modern and clean image that represents who we are. The card should be in black and white same as our logo. Minimal use of other colours is allowed.

Industry/Entity Type

Hair And Beauty

Contact Information for Business Card

The design should have the following information
salon name - TR Hair Studio
address - 2751 Birchfield Rd.E. Mississauga, ON L7P3K2
phone - 905 614-2870
website - trhairexample.ca
instagram - tr.hairstudio
twitter - @TR_HairStudio

Colors
000000
ffffff
474747

Requirements
Must have
• simple design, salon name, address, phone, website, instagram, twitter info
• Back of card should have the following:
• YOUR NEXT APPOINTMENT
• DATE
• TIME
Nice to have
• simple design, clear to see and read,
• predominantly black and white colour, minimal use of other colours is ok
Should not have
• many colours, various fonts

```html
<!DOCTYPE html>
<html lang="en">
<head>
<meta charset="utf-8">
<title>TR Hair Studio — Business Card</title>
<link rel="stylesheet" href="https://fonts.googleapis.com/css2?family=Montserrat:wght@400;500;700&family=Cormorant+Garamond:wght@500;600&display=swap">
<style>
  :root {
    --ink: #000000;
    --paper: #ffffff;
    --grey: #474747;
    --backdrop: #e6e6e6;
    --sans: "Montserrat", sans-serif;
    --serif: "Cormorant Garamond", serif;
  }
  * { box-sizing: border-box; margin: 0; padding: 0; }
  html, body { width: 1200px; height: 800px; overflow: hidden; }
  body {
    background: var(--backdrop);
    display: flex;
    align-items: center;
    justify-content: center;
    gap: 40px;
    font-family: var(--sans);
  }
  .card {
    position: relative;
    width: 540px;
    height: 310px;
    overflow: hidden;
    box-shadow: 0 6px 18px rgba(0,0,0,0.18);
  }
  .card-front { background: var(--paper); color: var(--ink); }
  .card-back { background: var(--ink); color: var(--paper); }
  .card-art { position: absolute; inset: 0; }

  .studio-name {
    position: absolute;
    left: 150px; top: 40px;
    font-family: var(--serif);
    font-weight: 600;
    font-size: 30px;
    letter-spacing: 0.5px;
  }
  .contact-list {
    position: absolute;
    left: 110px; top: 128px;
    list-style: none;
    color: var(--paper);
    font-size: 14px;
    line-height: 19px;
  }
  .contact-list li { display: flex; align-items: center; gap: 10px; }
  .contact-list svg { width: 12px; height: 12px; flex: none; }
  .address {
    position: absolute;
    left: 60px; top: 236px;
    display: flex; align-items: center; gap: 14px;
    font-size: 14px;
  }
  .address svg { width: 11px; height: 14px; }

  .brand-mark {
    position: absolute;
    font-family: var(--serif);
    font-weight: 600;
    color: var(--paper);
    white-space: nowrap;
  }
  .brand-mark-front { left: 460px; top: 210px; transform: translate(-50%, -50%); font-size: 30px; }
  .brand-mark-back { right: 40px; bottom: 38px; font-size: 38px; }

  .appointment-box {
    position: absolute;
    left: 0; top: 40px;
    width: 330px; height: 150px;
    background: var(--paper);
    color: var(--ink);
    padding: 26px 28px 0 44px;
    font-size: 13px;
    letter-spacing: 1px;
  }
  .appointment-title { margin-bottom: 16px; }
  .appointment-title strong { font-weight: 700; }
  .appointment-field { display: flex; align-items: flex-end; margin-bottom: 14px; }
  .appointment-field span { flex: none; }
  .appointment-field .fill-line {
    flex: 1;
    margin-left: 4px;
    border-bottom: 1.5px dotted var(--ink);
    height: 12px;
  }
</style>
</head>
<body>

  <section class="card card-front" aria-label="Card front">
    <svg class="card-art" viewBox="0 0 540 310" aria-hidden="true">
      <rect x="0" y="112" width="470" height="98" fill="var(--ink)"/>
      <circle cx="460" cy="210" r="70" fill="var(--paper)"/>
      <circle cx="460" cy="210" r="62" fill="var(--ink)"/>
    </svg>
    <h1 class="studio-name">TR Hair Studio</h1>
    <ul class="contact-list">
      <li><svg viewBox="0 0 12 12"><path d="M2.5 0.8 L4.6 3.2 L3.4 4.6 Q4.8 7.4 7.4 8.6 L8.8 7.4 L11.2 9.5 L9.8 11.2 Q4.5 11 0.8 2.2 Z" fill="var(--paper)"/></svg>905 614-2870</li>
      <li><svg viewBox="0 0 12 12"><circle cx="6" cy="6" r="5" fill="none" stroke="var(--paper)" stroke-width="1.3"/><ellipse cx="6" cy="6" rx="2.2" ry="5" fill="none" stroke="var(--paper)" stroke-width="1"/><line x1="1" y1="6" x2="11" y2="6" stroke="var(--paper)" stroke-width="1"/></svg>www.trhairexample.ca</li>
      <li><svg viewBox="0 0 12 12"><rect x="1" y="1" width="10" height="10" fill="var(--paper)"/></svg>tr.hairstudio</li>
      <li><svg viewBox="0 0 12 12"><circle cx="6" cy="6" r="5" fill="var(--paper)"/></svg>@TR_HairStudio</li>
    </ul>
    <p class="address">
      <svg viewBox="0 0 11 14" aria-hidden="true"><path d="M5.5 0.5 A5 5 0 0 1 10.5 5.5 Q10.5 8.5 5.5 13.5 Q0.5 8.5 0.5 5.5 A5 5 0 0 1 5.5 0.5 Z" fill="var(--ink)"/><circle cx="5.5" cy="5.3" r="1.8" fill="var(--paper)"/></svg>
      2751 Birchfield Rd.E. Mississauga, ON L7P3K2
    </p>
    <p class="brand-mark brand-mark-front">TR Hair</p>
  </section>

  <section class="card card-back" aria-label="Card back">
    <svg class="card-art" viewBox="0 0 540 310" aria-hidden="true">
      <line x1="0" y1="205" x2="520" y2="296" stroke="var(--paper)" stroke-width="1"/>
      <line x1="520" y1="240" x2="520" y2="296" stroke="var(--paper)" stroke-width="1"/>
    </svg>
    <div class="appointment-box">
      <p class="appointment-title">YOUR NEXT <strong>APPOINTMENT</strong></p>
      <p class="appointment-field"><span>DATE</span><span class="fill-line"></span></p>
      <p class="appointment-field"><span>TIME</span><span class="fill-line"></span></p>
    </div>
    <p class="brand-mark brand-mark-back">TR Hair</p>
  </section>

</body>
</html>
```